Wordpress Design for my Consulting Company

We want a WordPress site created for our new business. We have created a mock-up of the content we want on the site at https://marcobellweather.example.com/website-5

We are not attached to any of the pictures and just put stock stuff from bloq's editor, which we don't have rights to use outside of bloq.

We are NOT looking to just port this site to WordPress, we are looking for some creative ways to display the content in a more professional artistic sense.

I have included several logo files and a text file with the colors and Fonts used in the logo. We are not looking to change the logo or the colors used in the logo.

The Schedule appointment links to a page that embeds a bookslot.example calendar. https://bookslot.example.com/marco-bellweather/trailguide

The final website domain will be venturelanterns.example

Venture lanterns is a consulting company that works directly with the business owners and leaders of small businesses between 50-200 employees. We help companies make sure they have the right technology to meet their strategic goals. We are the anti-"Computer Guy" and we focus on business outcomes NOT cool technology gadgets.

The final design should communicate business growth and success.

Target Market(s)

Business Owners of companies with 50-200 employees

Coding

Coded - Design and coding required

Number of Pages Required

1 page

Font styles to use
Serif
Other font styles liked:
• Trajan Pro Bold, Open Sans

Requirements
Must have
• Should focus on consulting rather than technology.
• Should show the customer as the hero and we are just their guide.
• Must use the logo provided and the colors and fonts in the text file provided. Any other colors and fonts must be complementary.
• The design should scale for all devices computer, iPad, or phone
Should not have
• Should not focus on technology, we are the anti-"Computer Guy" and we focus on business outcomes NOT cool technology gadgets.

```html
<!DOCTYPE html>
<html lang="en">
<head>
<meta charset="utf-8">
<title>Venture Lanterns — Website Design</title>
<link href="https://fonts.googleapis.com/css2?family=Cinzel:wght@400;600&family=Open+Sans:wght@300;400;600&display=swap" rel="stylesheet">
<style>
:root{
  --board:#ececec;
  --slate:#3e4b55;
  --slate-deep:#34414a;
  --slate-light:#55636c;
  --orange:#d5784a;
  --peach:#f6e2d6;
  --ink:#4a4a4a;
  --muted:#8a8a8a;
  --white:#ffffff;
}
*{margin:0;padding:0;box-sizing:border-box}
html,body{width:1200px;height:1200px;overflow:hidden;background:var(--board)}
body{position:relative;font-family:"Open Sans",Arial,sans-serif;color:var(--ink)}
.column{position:absolute;top:0;width:506px;height:1200px;overflow:hidden}
.column--left{left:88px}
.column--right{left:606px}
.abs{position:absolute}
.center{left:0;right:0;text-align:center}
.serif-caps{font-family:"Cinzel",Georgia,serif;font-weight:400}
.accent{color:var(--orange)}
.photo{position:absolute;left:0;width:100%}
.photo--desk{top:0;height:270px;background:linear-gradient(160deg,#56646d 0%,#45535c 45%,#3b4851 100%)}
.photo--chess{top:0;height:301px;background:radial-gradient(ellipse at 60% 75%,#4b5963 0%,#3b4851 55%,#334049 100%)}
.photo--slate{top:754px;height:446px;background:linear-gradient(180deg,var(--slate) 0%,#3a474f 100%)}
.photo--city{top:833px;height:367px;background:linear-gradient(200deg,#4a5760 0%,#3d4a53 50%,#34414a 100%)}
.panel-white{position:absolute;left:0;width:100%;background:var(--white)}
.btn{position:absolute;border-radius:10px;font-size:6.5px;font-weight:600;display:flex;align-items:center;justify-content:center;height:15px;width:95px}
.btn--solid{background:var(--orange);color:var(--white)}
.btn--outline{border:1px solid #e7b9a2;color:var(--orange);background:var(--white)}
.site-logo{left:44px;top:20px;display:flex;align-items:center;gap:6px}
.site-logo__mark{width:12px;height:12px;border-radius:50%;background:var(--orange)}
.site-logo__name{font-family:"Cinzel",Georgia,serif;font-size:6.5px;color:var(--white);line-height:1.1}
.site-logo__tag{font-size:3.5px;color:#c9d0d4;letter-spacing:.3px}
.nav{top:27px;font-size:6.5px;color:var(--white)}
.nav-rule{left:42px;width:422px;top:46px;height:1px;background:rgba(255,255,255,.45)}
.hero-title{top:112px;font-size:17px;color:var(--white);letter-spacing:.3px}
.hero-sub{top:137px;font-size:8px;color:#dfe4e7;font-weight:300}
.slider-dots{top:232px;left:0;right:0;display:flex;justify-content:center;gap:4px}
.slider-dots span{width:13px;height:1.5px;background:rgba(255,255,255,.55)}
.slider-dots span:first-child{background:var(--orange)}
.slider-caption{top:241px;font-size:6px;color:var(--white)}
.section-title{font-size:12.5px;color:#555}
.pain{position:absolute;width:140px;text-align:center;font-size:7.5px;line-height:12.8px;color:var(--muted);font-weight:300}
.pain svg{display:block;margin:0 auto 8px}
.statement{font-size:8px;line-height:13.6px;color:#e6eaec;letter-spacing:.2px}
.testimonial{left:72px;top:886px;width:362px;height:125px;border-radius:6px;background:rgba(255,255,255,.06)}
.avatar{left:230px;top:862px;width:46px;height:46px;border-radius:50%;background:radial-gradient(circle at 50% 40%,#b39a86 0%,#7a5e4c 60%,#4d3c33 100%);border:2px solid #6d5546}
.quote{top:925px;left:110px;width:286px;text-align:center;font-size:5.8px;line-height:10.4px;color:#d9dee1}
.quote-author{top:962px;left:0;right:0;text-align:center;font-size:6px;line-height:9px;color:var(--white)}
.quote-author b{font-weight:600}
.arrow{top:943px;font-size:10px;color:#dfe4e7}
.closing{top:1147px;left:20px;right:20px;font-size:12.5px;line-height:20.5px;color:var(--white);text-align:center}
.hero-statement{top:144px;left:50px;right:50px;font-size:12.5px;line-height:20.5px;color:var(--white);text-align:center}
.step{position:absolute;width:180px;text-align:center}
.step__icon{width:62px;height:62px;border-radius:50%;background:var(--peach);margin:0 auto;display:flex;align-items:center;justify-content:center}
.step__name{margin-top:12px;font-size:9.5px;color:#333}
.step__text{margin-top:8px;font-size:7.5px;line-height:12.8px;color:var(--muted);font-weight:300}
.contact-title{left:42px;top:889px;font-size:13px;color:var(--white)}
.contact-row{left:42px;display:flex;gap:8px;font-size:8px;line-height:11.5px;color:#e3e7ea;align-items:flex-start}
.field{position:absolute;border:1px solid #aab4ba;font-family:"Cinzel",Georgia,serif;font-size:5px;color:#c8d0d5;padding:4px 5px}
.send{left:382px;top:1069px;width:82px;height:17px;background:var(--orange);color:#f6dccd;font-family:"Cinzel",Georgia,serif;font-size:5px;display:flex;align-items:center;justify-content:center}
.footer-rule{left:42px;width:422px;top:1168px;height:1px;background:rgba(255,255,255,.3)}
.footer-note{top:1180px;font-size:5.8px;color:#c9d0d4}
</style>
</head>
<body>

<!-- LEFT COLUMN -->
<section class="column column--left">
  <div class="photo photo--desk" role="img" aria-label="Dim photo of business people reviewing charts at a desk with a laptop"></div>

  <div class="abs site-logo">
    <span class="site-logo__mark"></span>
    <div>
      <div class="site-logo__name">Venture Lanterns</div>
      <div class="site-logo__tag">Guiding your business forward</div>
    </div>
  </div>
  <div class="abs nav" style="left:355px">Home</div>
  <div class="abs nav" style="left:394px">Schedule Appointment</div>
  <div class="abs nav-rule"></div>

  <h1 class="abs center hero-title serif-caps">Technology Advisors That <span class="accent">“Get”</span> Business.</h1>
  <p class="abs center hero-sub">We help you leverage technology to create a competitive advantage.</p>
  <div class="btn btn--solid" style="left:206px;top:169px">Schedule Appointment</div>
  <div class="abs slider-dots"><span></span><span></span><span></span><span></span><span></span><span></span></div>
  <p class="abs center slider-caption">We Get... Reducing Time to Decision</p>

  <div class="panel-white" style="top:270px;height:484px"></div>
  <h2 class="abs center section-title serif-caps" style="top:318px">Are you tired of <span class="accent">“Computer Guys”</span> that...</h2>

  <svg width="0" height="0" style="position:absolute">
    <defs>
      <symbol id="tick" viewBox="0 0 20 20">
        <circle cx="10" cy="10" r="9" fill="var(--peach)"/>
        <circle cx="10" cy="10" r="5" fill="none" stroke="var(--orange)" stroke-width="1"/>
        <path d="M7.5 10l2 2 4-4.5" fill="none" stroke="var(--orange)" stroke-width="1.1"/>
      </symbol>
    </defs>
  </svg>

  <div class="pain" style="left:83px;top:362px"><svg width="18" height="18"><use href="#tick"/></svg>Don't want to be involved in business strategy.</div>
  <div class="pain" style="left:282px;top:362px"><svg width="18" height="18"><use href="#tick"/></svg>Give you the excuse, “You never asked.”</div>
  <div class="pain" style="left:83px;top:449px"><svg width="18" height="18"><use href="#tick"/></svg>Say “No!” but do not give options on how to achieve your business outcome.</div>
  <div class="pain" style="left:282px;top:449px"><svg width="18" height="18"><use href="#tick"/></svg>Recommend technology when a simple process or policy change would have the same effect.</div>
  <div class="pain" style="left:83px;top:563px"><svg width="18" height="18"><use href="#tick"/></svg>Can't explain how a technology will create business value, but insist it is necessary.</div>
  <div class="pain" style="left:282px;top:563px"><svg width="18" height="18"><use href="#tick"/></svg>Suggest expensive solutions that are just thrown away, soon after they are deployed.</div>

  <div class="btn btn--outline" style="left:206px;top:677px">Schedule Appointment</div>

  <div class="photo photo--slate" role="img" aria-label="Muted slate background photo"></div>
  <p class="abs statement serif-caps" style="top:785px;left:76px;width:354px;text-align:center">We get the frustration of working with consultants and experts who don't listen or take the time to understand your company goals and vision. We believe technology should serve your business, not the other way around.</p>

  <div class="abs testimonial"></div>
  <div class="abs avatar" role="img" aria-label="Portrait photo of the client giving the testimonial"></div>
  <p class="abs quote">“We get the frustration of working with consultants and experts who don't listen or take the time to understand your company goals and vision. We believe technology should serve your business, not the other way around.”</p>
  <p class="abs quote-author"><b>- Dale Whitcomb</b><br>Pastor, Operations and Leadership Development<br>Cedar Hollow Fellowship</p>
  <div class="abs arrow" style="left:82px">‹</div>
  <div class="abs arrow" style="left:421px">›</div>

  <p class="abs closing serif-caps">Computer guys frustrate business leaders because they don't have a business mindset. Venture Lanterns advises on strategy that helps companies apply technology to gain</p>
</section>

<!-- RIGHT COLUMN -->
<section class="column column--right">
  <div class="photo photo--chess" role="img" aria-label="Dark photo of chess pieces on a board"></div>
  <p class="abs hero-statement serif-caps">Computer guys frustrate business leaders because they don't have a business mindset. Venture Lanterns advises on strategy that helps companies apply technology to gain a competitive advantage.</p>
  <div class="btn btn--solid" style="left:327px;top:253px">Schedule Appointment</div>

  <div class="panel-white" style="top:301px;height:532px"></div>
  <h2 class="abs center section-title serif-caps" style="top:357px;line-height:17px">The four steps to aligning technology to your<br>business strategy!</h2>

  <div class="step" style="left:64px;top:439px">
    <div class="step__icon">
      <svg width="38" height="38" viewBox="0 0 38 38" fill="none" stroke="var(--orange)" stroke-width="1.2">
        <circle cx="16" cy="16" r="11"/><circle cx="16" cy="16" r="7.5"/>
        <path d="M24 24l8 8"/><path d="M12 19v-3M15 19v-5M18 19v-4M21 19v-6"/>
      </svg>
    </div>
    <div class="step__name">Discover</div>
    <div class="step__text">Identify what is going on behind the scenes, and create a snapshot of the current infrastructure.</div>
  </div>

  <div class="step" style="left:274px;top:439px">
    <div class="step__icon">
      <svg width="40" height="40" viewBox="0 0 40 40" fill="none" stroke="var(--orange)" stroke-width="1.2">
        <rect x="12" y="5" width="24" height="16"/><path d="M16 17l5-5 4 3 7-7"/>
        <circle cx="9" cy="14" r="3"/><path d="M5 28v-7h8v7"/>
        <circle cx="22" cy="29" r="3"/><circle cx="31" cy="29" r="3"/><path d="M4 33h32"/>
      </svg>
    </div>
    <div class="step__name">Prioritize</div>
    <div class="step__text">Meet to decide which solutions and policies will have the greatest impact on reaching the companies goals.</div>
  </div>

  <div class="step" style="left:64px;top:615px">
    <div class="step__icon">
      <svg width="38" height="38" viewBox="0 0 38 38" fill="none" stroke="var(--orange)" stroke-width="1.2">
        <circle cx="19" cy="19" r="5"/><circle cx="19" cy="19" r="10" stroke-dasharray="4 2.3"/>
        <path d="M19 3v4M19 31v4M3 19h4M31 19h4"/>
      </svg>
    </div>
    <div class="step__name">Implement</div>
    <div class="step__text">Implement those things that will give the greatest return on investment.</div>
  </div>

  <div class="step" style="left:274px;top:615px">
    <div class="step__icon">
      <svg width="40" height="40" viewBox="0 0 40 40" fill="none" stroke="var(--orange)" stroke-width="1.2">
        <rect x="5" y="6" width="30" height="26"/><path d="M5 11h30"/>
        <path d="M13 16v14M25 18a4 4 0 1 0 6 0v12"/>
      </svg>
    </div>
    <div class="step__name">Maintain</div>
    <div class="step__text">Create a system that keeps your technology aligned as strategy adjusts over time.</div>
  </div>

  <div class="photo photo--city" role="img" aria-label="Dark upward photo of city office towers"></div>
  <h2 class="abs contact-title serif-caps">Contact Us</h2>

  <div class="abs contact-row" style="top:923px">
    <svg width="11" height="12" viewBox="0 0 11 12" fill="none" stroke="var(--orange)" stroke-width="1"><path d="M5.5 11.5S1 7 1 4.5a4.5 4.5 0 0 1 9 0C10 7 5.5 11.5 5.5 11.5z"/><circle cx="5.5" cy="4.5" r="1.6"/></svg>
    <span>4120 Harlow Ridge Parkway South,<br>Suite 310, Millbrook, TX 77910</span>
  </div>
  <div class="abs contact-row" style="top:966px">
    <svg width="11" height="10" viewBox="0 0 11 10" fill="none" stroke="var(--orange)" stroke-width="1"><rect x=".5" y="1" width="10" height="8"/><path d="M.5 1.5l5 4 5-4"/></svg>
    <span>hello@venturelanterns.example</span>
  </div>
  <div class="abs contact-row" style="top:997px">
    <svg width="11" height="11" viewBox="0 0 11 11" fill="none" stroke="var(--orange)" stroke-width="1"><path d="M2 1l2 2.5-1 1.5a6 6 0 0 0 3 3l1.5-1L10 9l-1.5 1.5C5 10 1 6 .5 2.5z"/></svg>
    <span>(555) 210-4837</span>
  </div>

  <div class="field" style="left:245px;top:890px;width:107px;height:17px">Name *</div>
  <div class="field" style="left:357px;top:890px;width:107px;height:17px">Email *</div>
  <div class="field" style="left:245px;top:914px;width:219px;height:17px">Subject</div>
  <div class="field" style="left:245px;top:939px;width:219px;height:17px">Phone</div>
  <div class="field" style="left:245px;top:963px;width:219px;height:17px">Address</div>
  <div class="field" style="left:245px;top:988px;width:219px;height:70px">Message</div>
  <div class="abs send">Send</div>

  <div class="abs footer-rule"></div>
  <p class="abs center footer-note">©2018 by Venture Lanterns</p>
</section>

</body>
</html>
```